Calder Surgery description videos

I am a surgeon performing a relatively uncommon group of procedures for patients with chronic pain. I would like to start a YouTube channel featuring videos that explain the process, procedures, recovery, etc. I would like it to be professional, and easily found on internet searches. Example https://vidmora.example/Qk7rTz2Lp_m

Target Market(s)

Patients with chronic nerve pain

Industry/Entity Type

Medicine

Requirements
Must have
• Excellent search ability on google. Professional look.

```html
<!DOCTYPE html>
<html lang="en">
<head>
<meta charset="UTF-8">
<title>Chronic Pain – Video Thumbnail</title>
<link href="https://fonts.googleapis.com/css2?family=Lato:wght@400;700;900&display=swap" rel="stylesheet">
<style>
  :root {
    --backdrop: #9a9a9a;
    --deep-blue: #1636a8;
    --royal-blue: #2447c2;
    --label-ink: #13289a;
    --teal: #2fd3d6;
    --white: #ffffff;
    --photo-light: #dfe6f4;
    --photo-mid: #a9b8e0;
    --photo-shirt: #8ea4dc;
  }
  * { margin: 0; padding: 0; box-sizing: border-box; }
  html, body {
    width: 1200px; height: 732px; overflow: hidden;
    background: var(--backdrop);
    font-family: "Lato", sans-serif;
  }
  .thumbnail {
    position: absolute;
    left: 58px; top: 62px;
    width: 1084px; height: 609px;
    overflow: hidden;
  }
  .thumbnail__photo {
    position: absolute; inset: 0;
    background:
      radial-gradient(ellipse 30% 55% at 78% 35%, var(--photo-shirt) 0%, transparent 70%),
      radial-gradient(ellipse 35% 40% at 75% 85%, #cfd2dc 0%, transparent 75%),
      linear-gradient(90deg, var(--photo-mid) 0%, var(--photo-light) 60%, #eef1f8 100%);
  }
  .thumbnail__tint {
    position: absolute; inset: 0;
    background: linear-gradient(90deg,
      var(--deep-blue) 0%,
      rgba(30, 64, 190, 0.92) 30%,
      rgba(50, 90, 200, 0.6) 55%,
      rgba(60, 100, 210, 0.15) 72%,
      rgba(60, 100, 210, 0) 85%);
  }
  .thumbnail__accent {
    position: absolute; left: 0; top: 0;
    width: 1084px; height: 609px;
  }
  .category-marker {
    position: absolute; left: 0; top: 148px;
    width: 10px; height: 35px;
    background: var(--teal);
  }
  .category-label {
    position: absolute; left: 52px; top: 148px;
    width: 320px; height: 35px;
    background: var(--white);
    color: var(--label-ink);
    font-weight: 900; font-size: 22px;
    letter-spacing: 11px;
    white-space: nowrap;
    display: flex; align-items: center;
    padding-left: 12px;
  }
  .headline {
    position: absolute; left: 52px; top: 205px;
    width: 640px;
    color: var(--white);
    font-weight: 400; font-size: 51px;
    line-height: 57px;
    letter-spacing: -0.5px;
    white-space: nowrap;
  }
  .channel-rule {
    position: absolute; left: 52px; top: 460px;
    width: 230px; height: 2px;
    background: var(--teal);
  }
  .channel-name {
    position: absolute; left: 52px; top: 474px;
    color: var(--white);
    font-weight: 700; font-size: 14px;
    letter-spacing: 7px;
    white-space: nowrap;
  }
</style>
</head>
<body>
  <main class="thumbnail">
    <div class="thumbnail__photo" role="img" aria-label="Photo of a woman in a blue shirt sitting on an office chair, holding her lower back in pain, with a desk and monitor behind her"></div>
    <div class="thumbnail__tint"></div>
    <svg class="thumbnail__accent" viewBox="0 0 1084 609" aria-hidden="true">
      <polygon points="0,511 0,609 120,609" fill="#1230a0" opacity="0.55"/>
      <line x1="0" y1="508" x2="122" y2="609" stroke="#3c63e0" stroke-width="5"/>
    </svg>
    <div class="category-marker"></div>
    <div class="category-label">CHRONIC PAIN</div>
    <h1 class="headline">What a patient may<br>expect following surgery<br>for a nerve-related<br>problem.</h1>
    <div class="channel-rule"></div>
    <div class="channel-name">CALDER SURGERY</div>
  </main>
</body>
</html>
```